Lantern Hearthworks Business Cards

Looking to create simple business cards that highlight our unique three sided triangle fire pit design with the colors and font of our logo, listed below.

Requirements
Must have
• Looking for something simple that includes a picture of our fire pit with name, website (lanternhearthworks.com), phone number and email. Want to keep the color mostly orange and black.
• Font is gotham(medium) and orange color code is #ee6e22

```html
<!DOCTYPE html>
<html lang="en">
<head>
<meta charset="UTF-8">
<title>Lantern Hearthworks Business Cards</title>
<link href="https://fonts.googleapis.com/css2?family=Montserrat:wght@400;500;600&display=swap" rel="stylesheet">
<style>
  :root {
    --page-bg: #5b5c5e;
    --card-white: #ffffff;
    --brand-orange: #ee6e22;
    --brand-gray: #6d6e70;
    --ink: #58595b;
    --char-dark: #1f1f20;
    --char-mid: #3a3a3b;
  }
  * { margin: 0; padding: 0; box-sizing: border-box; }
  html, body {
    width: 1200px;
    height: 800px;
    overflow: hidden;
    background: var(--page-bg);
    font-family: "Montserrat", Arial, sans-serif;
  }
  .canvas {
    position: relative;
    width: 1200px;
    height: 800px;
  }
  .card {
    position: absolute;
    left: 350px;
    width: 507px;
    height: 290px;
    border-radius: 18px;
    overflow: hidden;
  }
  .card-front { top: 70px; background: var(--card-white); }
  .card-back { top: 433px; }

  .front-wave {
    position: absolute;
    left: 0; top: 0;
    width: 507px; height: 290px;
  }

  .brand {
    position: absolute;
    left: 24px;
    top: 106px;
    display: flex;
    align-items: center;
  }
  .brand-dot {
    width: 34px; height: 34px;
    border-radius: 50%;
    background: var(--brand-orange);
    margin-left: 20px;
    margin-right: 25px;
  }
  .brand-divider {
    width: 1px;
    height: 77px;
    background: var(--brand-gray);
    margin-right: 9px;
  }
  .brand-name {
    color: var(--brand-orange);
    font-weight: 500;
    font-size: 15px;
    line-height: 1.2;
    letter-spacing: 1.6px;
  }

  .person {
    position: absolute;
    left: 270px;
    top: 91px;
  }
  .person-name {
    color: var(--brand-orange);
    font-weight: 600;
    font-size: 21px;
    letter-spacing: 0.6px;
    line-height: 1;
  }
  .person-role {
    color: var(--ink);
    font-weight: 400;
    font-size: 13.5px;
    margin-top: 4px;
  }
  .contact-list {
    list-style: none;
    margin-top: 14px;
  }
  .contact-item {
    display: flex;
    align-items: center;
    color: var(--ink);
    font-size: 12.5px;
    height: 20px;
    letter-spacing: 0.1px;
    white-space: nowrap;
  }
  .contact-icon {
    width: 13px; height: 13px;
    margin-right: 11px;
    flex: none;
  }

  .fire-pit-photo {
    width: 100%;
    height: 100%;
    background:
      radial-gradient(ellipse 70px 60px at 59% 52%, rgba(238,110,34,0.85), rgba(238,110,34,0) 100%),
      radial-gradient(ellipse 110px 100px at 52% 56%, #0c0c0c, rgba(12,12,12,0) 100%),
      linear-gradient(135deg, var(--char-mid), var(--char-dark) 60%, var(--char-mid));
  }
</style>
</head>
<body>
<main class="canvas">

  <section class="card card-front">
    <svg class="front-wave" viewBox="0 0 507 290" aria-hidden="true">
      <path d="M0 241 Q170 266 260 268 Q400 266 507 255 V290 H0 Z" fill="var(--brand-orange)"/>
      <path d="M165 262 Q360 258 507 236 L507 242 Q360 263 165 264 Z" fill="var(--brand-orange)"/>
      <path d="M170 265 Q360 263 507 247 L507 253 Q360 269 170 267 Z" fill="var(--brand-gray)"/>
      <path d="M180 268.5 Q360 268 507 256 L507 258 Q360 271 180 270 Z" fill="var(--card-white)"/>
    </svg>

    <div class="brand">
      <span class="brand-dot"></span>
      <span class="brand-divider"></span>
      <p class="brand-name">LANTERN<br>HEARTHWORKS</p>
    </div>

    <div class="person">
      <h1 class="person-name">OWEN CARTER</h1>
      <p class="person-role">Founder | CEO</p>
      <ul class="contact-list">
        <li class="contact-item">
          <svg class="contact-icon" viewBox="0 0 24 24" aria-hidden="true">
            <path d="M6.6 10.8a15 15 0 0 0 6.6 6.6l2.2-2.2a1 1 0 0 1 1-.25 11.4 11.4 0 0 0 3.6.57 1 1 0 0 1 1 1V20a1 1 0 0 1-1 1A17 17 0 0 1 3 4a1 1 0 0 1 1-1h3.5a1 1 0 0 1 1 1c0 1.25.2 2.45.57 3.57a1 1 0 0 1-.25 1z" fill="var(--brand-orange)"/>
          </svg>
          123 456 7890
        </li>
        <li class="contact-item">
          <svg class="contact-icon" viewBox="0 0 24 24" aria-hidden="true">
            <rect x="1" y="4" width="22" height="16" fill="var(--brand-orange)"/>
            <path d="M1 4 L12 13 L23 4 M1 20 L9 11 M23 20 L15 11" stroke="#fff" stroke-width="1.6" fill="none"/>
          </svg>
          hi@lanternhearthworks.com
        </li>
        <li class="contact-item">
          <svg class="contact-icon" viewBox="0 0 24 24" aria-hidden="true">
            <circle cx="12" cy="12" r="11" fill="var(--brand-orange)"/>
            <g stroke="#fff" stroke-width="1.2" fill="none">
              <ellipse cx="12" cy="12" rx="4.5" ry="9"/>
              <path d="M3 12h18M4.5 7.5h15M4.5 16.5h15M12 3v18"/>
            </g>
          </svg>
          www.lanternhearthworks.com
        </li>
      </ul>
    </div>
  </section>

  <section class="card card-back">
    <div class="fire-pit-photo" role="img" aria-label="Photo from above of a triangular black steel fire pit with burning logs and orange flames, set on dark gravel"></div>
  </section>

</main>
</body>
</html>
```